New website ArchitekturAtelier Brunnmatt

ArchitekturAtelier Brunnmatt GmbH from Bonaduz requires a complete redesign of its website, atelier-brunnmatt-example.ch. The established architectural firm seeks to present its projects and expertise in a contemporary, professional manner with a modern, professional website. The new website should include the Projects/Portfolio, References, Company Profile, and Contact sections, similar to the existing site. The desired design is minimalist, trustworthy, with clean lines and professional colors that appeals to both business and private customers and is optimized for responsiveness on all devices. The cube elements from the existing logo can be integrated into the website design, playing with the primary colors. The logo font Avantgarde can serve as the typographic basis.
Target Market(s)
Developers (public & private)
Industry/Entity Type
Architektur
Number of Pages Required
1 page
Requirements
Must have
- Logo must remain (colored cubes)
Nice to have
- simple, easy user guidance

```html
<!DOCTYPE html>
<html lang="en">
<head>
<meta charset="utf-8">
<title>ArchitekturAtelier Brunnmatt GmbH</title>
<link href="https://fonts.googleapis.com/css2?family=Jost:wght@300;400;500;600&display=swap" rel="stylesheet">
<style>
:root{
  --red:#f20f0f;
  --ink:#111111;
  --muted:#6b6b6b;
  --dark:#1d222b;
  --panel:#ececec;
  --line:#d6d6d6;
  --white:#ffffff;
  --footer:#050505;
}
*{margin:0;padding:0;box-sizing:border-box}
html,body{width:1200px;height:4923px;overflow:hidden}
body{position:relative;background:var(--white);font-family:'Jost',sans-serif;color:var(--ink)}
.abs{position:absolute}
.btn{position:absolute;background:var(--red);color:var(--white);font-weight:600;font-size:13px;display:flex;align-items:center;justify-content:center}
.ph{position:absolute}
/* header */
.topbar{left:363px;top:0;width:837px;height:32px;background:var(--ink);color:#ddd;font-size:12px}
.topbar span{position:absolute;top:8px;display:flex;align-items:center;gap:8px}
.brand{left:61px;top:26px;width:150px;font-size:15px;line-height:18px;font-weight:500;color:var(--ink)}
.nav a{position:absolute;top:64px;font-size:13px;color:var(--ink);text-decoration:none}
.nav-mark{left:422px;top:56px;width:9px;height:9px;background:var(--red)}
/* hero */
.hero-bg{left:22px;top:111px;width:1178px;height:663px;background:linear-gradient(120deg,#f4f4f4 0%,#fbfbfb 45%,#eeeeee 100%)}
.hero-kicker{left:59px;top:312px;font-size:22px;font-weight:600;color:var(--red)}
.hero-title{left:50px;top:346px;font-size:50px;line-height:60px;font-weight:500}
.hero-text{left:52px;top:484px;width:340px;font-size:11.5px;line-height:14px;color:#555}
/* about */
.about-title{left:501px;top:976px;font-size:40px;line-height:50px;font-weight:500}
.about-text{left:506px;top:1145px;width:585px;font-size:12px;line-height:15px;color:#555}
.feat h4{position:absolute;font-size:15px;font-weight:500}
.feat p{position:absolute;font-size:12px;line-height:15px;color:#666;width:200px}
/* services */
.section-title{position:absolute;font-size:38px;font-weight:500}
.card{position:absolute;top:1850px;width:225px;height:367px;background:var(--white);border:1px solid var(--line)}
.card .ph{left:0;top:0;width:223px;height:183px}
.card h3{position:absolute;left:27px;top:206px;font-size:27px;line-height:32px;font-weight:500}
.card p{position:absolute;left:27px;top:274px;width:180px;font-size:11px;line-height:14px;color:#777}
.card .go{position:absolute;left:27px;top:343px;width:45px;height:42px;background:var(--red);display:flex;align-items:center;justify-content:center}
/* projects */
.filters{right:118px;top:2392px;font-size:19px;color:var(--ink)}
.filters em{font-style:normal;color:var(--red)}
.slide-nav{top:2840px;width:19px;height:19px;background:#999;color:#fff;font-size:10px;display:flex;align-items:center;justify-content:center}
/* contact */
.contact-band{left:0;top:2994px;width:1200px;height:536px}
.contact-item h4{position:absolute;font-size:20px;font-weight:500;color:var(--white)}
.contact-item p{position:absolute;font-size:14px;line-height:15px;color:#d5d5d5}
.form{left:667px;top:3094px;width:390px;height:543px;background:var(--panel)}
.field{position:absolute;left:29px;width:329px;height:44px;background:var(--white);font-size:12px;color:#777;padding:14px 20px}
/* blog */
.blog-label{position:absolute;left:138px;width:220px;height:96px;background:#0b0b0b;color:#fff}
.blog-label b{position:absolute;left:34px;top:24px;font-size:16px;line-height:22px;font-weight:600;width:170px}
.vdate{position:absolute;font-size:10px;font-weight:600;transform:rotate(-90deg);transform-origin:left top;white-space:nowrap}
/* footer */
.footer{left:0;top:4544px;width:1200px;height:379px;background:var(--footer);color:var(--white)}
.footer h5{position:absolute;top:84px;font-size:13px;font-weight:600}
.footer .lnk{position:absolute;left:380px;font-size:14px}
.footer .ci{position:absolute;left:621px;font-size:14px;line-height:19px;width:270px}
</style>
</head>
<body>

<!-- header -->
<div class="abs topbar">
  <span style="left:59px"><svg width="14" height="12" viewBox="0 0 14 12"><rect x="1" y="2" width="12" height="9" fill="var(--red)"/><path d="M1 2l6 5 6-5" stroke="#000" fill="none"/></svg>architektur@atelier-brunnmatt-example.ch</span>
  <span style="left:318px"><svg width="13" height="13" viewBox="0 0 24 24"><path d="M6.6 10.8a15 15 0 006.6 6.6l2.2-2.2c.3-.3.7-.4 1-.2 1.1.4 2.3.6 3.6.6.6 0 1 .4 1 1V20c0 .6-.4 1-1 1C10.6 21 3 13.4 3 4c0-.6.4-1 1-1h3.5c.6 0 1 .4 1 1 0 1.3.2 2.5.6 3.6.1.3 0 .7-.2 1z" fill="var(--red)"/></svg>099 555 01 40</span>
</div>
<div class="abs brand">ArchitekturAtelier Brunnmatt GmbH</div>
<div class="abs nav-mark"></div>
<nav class="nav">
  <a style="left:422px">Home</a><a style="left:506px">About</a><a style="left:596px">Services</a><a style="left:701px">Projects</a><a style="left:810px">Contact</a>
</nav>
<div class="btn" style="left:975px;top:57px;width:135px;height:37px">Get a Quote</div>

<!-- hero -->
<div class="abs hero-bg"></div>
<div class="abs hero-kicker">Welcome To</div>
<h1 class="abs hero-title">ArchitekturAtelier<br>Brunnmatt GmbH</h1>
<p class="abs hero-text">we believe architecture is more than just structures — it's about creating experiences, enriching environments, and shaping the future.</p>
<div class="btn" style="left:52px;top:552px;width:138px;height:34px">Get a Quote</div>
<div class="ph" role="img" aria-label="White angular museum building" style="left:634px;top:216px;width:197px;height:183px;background:linear-gradient(160deg,#c9d4e0,#8e9caf 60%,#e8ebef)"></div>
<div class="ph" role="img" aria-label="Building facade tinted blue" style="left:908px;top:183px;width:195px;height:182px;background:linear-gradient(150deg,#5a63ff,#2b2ee0)"></div>
<div class="ph" role="img" aria-label="Interior tinted yellow" style="left:634px;top:432px;width:197px;height:183px;background:linear-gradient(150deg,#f2f53a,#c9cc10)"></div>
<div class="ph" role="img" aria-label="Faceted white building against grey sky" style="left:860px;top:432px;width:197px;height:183px;background:linear-gradient(160deg,#e3e6ea,#9aa3ae)"></div>
<div class="ph" role="img" aria-label="White staircase interior with armchairs" style="left:634px;top:648px;width:197px;height:176px;background:linear-gradient(160deg,#dcdcdc,#9a9a9a)"></div>
<div class="ph" role="img" aria-label="Modern white villa with glass front" style="left:860px;top:648px;width:197px;height:183px;background:linear-gradient(160deg,#cfd8e2,#8c7a66)"></div>

<!-- about -->
<div class="ph" role="img" aria-label="Concrete and glass tower seen from below" style="left:52px;top:925px;width:340px;height:562px;background:linear-gradient(110deg,#5d7c93 0%,#8a8a88 45%,#b5b3ae 100%)"></div>
<h2 class="abs about-title">Innovative Architecture<br>Rooted in Purpose and<br>Vision.</h2>
<p class="abs about-text">we believe architecture is more than just structures — it's about creating experiences, enriching environments, and shaping the future. With a passion for design and a commitment to excellence, we transform ideas into timeless architectural solutions that blend functionality, aesthetics, and sustainability.</p>
<div class="btn" style="left:501px;top:1244px;width:155px;height:34px">More About Us</div>
<div class="feat">
  <svg class="abs" style="left:495px;top:1338px" width="84" height="84" viewBox="0 0 84 84" fill="none" stroke="#111" stroke-width="2.5"><rect x="8" y="10" width="68" height="62"/><path d="M8 22h68M20 34h24v22H20zM52 34h14M52 44h14M52 54h14M44 72l20-20 6 6-20 20z"/></svg>
  <h4 style="left:598px;top:1340px">Modern Design</h4>
  <p style="left:601px;top:1369px">it's about creating experiences, enriching environments, and shaping the future.</p>
  <svg class="abs" style="left:822px;top:1338px" width="88" height="84" viewBox="0 0 88 84" fill="none" stroke="#111" stroke-width="2.5"><path d="M44 6L82 26 44 46 6 26z"/><path d="M6 40l38 20 38-20M6 54l38 20 38-20"/><path d="M25 16l38 20M63 16L25 36M44 6v40M16 21h56M16 31h56" stroke-width="1.5"/></svg>
  <h4 style="left:931px;top:1336px">Quality Work</h4>
  <p style="left:931px;top:1358px">it's about creating experiences, enriching environments, and shaping the future.</p>
</div>

<!-- what we do -->
<div class="ph" role="img" aria-label="Dark modern building at dusk" style="left:0;top:1626px;width:1200px;height:428px;background:linear-gradient(100deg,#1e2530 0%,#2c3544 50%,#1b212b 100%)"></div>
<h2 class="section-title" style="left:0;width:1200px;text-align:center;top:1726px;color:var(--white)">What We Do</h2>
<div class="card" style="left:73px">
  <div class="ph" role="img" aria-label="Angular glass museum building" style="background:linear-gradient(160deg,#dfe5ec,#7f8d9c)"></div>
  <h3>Architectural<br>Design</h3><p>it's about creating experiences, enriching environments, and shaping the future.</p>
  <div class="go"><svg width="20" height="20" viewBox="0 0 20 20"><path d="M18 2L2 9l7 2 2 7z" fill="#fff"/></svg></div>
</div>
<div class="card" style="left:348px">
  <div class="ph" role="img" aria-label="Modern kitchen interior" style="background:linear-gradient(160deg,#c9c4bb,#4a4743)"></div>
  <h3>Home<br>Interior</h3><p>it's about creating experiences, enriching environments, and shaping the future.</p>
  <div class="go"><svg width="20" height="20" viewBox="0 0 20 20"><path d="M18 2L2 9l7 2 2 7z" fill="#fff"/></svg></div>
</div>
<div class="card" style="left:625px">
  <div class="ph" role="img" aria-label="Glass building at night with reflections" style="background:linear-gradient(170deg,#9cc4ea,#1e3c6e)"></div>
  <h3>Exterior<br>Design</h3><p>it's about creating experiences, enriching environments, and shaping the future.</p>
  <div class="go"><svg width="20" height="20" viewBox="0 0 20 20"><path d="M18 2L2 9l7 2 2 7z" fill="#fff"/></svg></div>
</div>
<div class="card" style="left:900px">
  <div class="ph" role="img" aria-label="Modern house with red accents and a classic car" style="background:linear-gradient(170deg,#a9c8d6,#d8522f 70%,#bcb7ae)"></div>
  <h3>Resilient<br>Structures</h3><p>it's about creating experiences, enriching environments, and shaping the future.</p>
  <div class="go"><svg width="20" height="20" viewBox="0 0 20 20"><path d="M18 2L2 9l7 2 2 7z" fill="#fff"/></svg></div>
</div>

<!-- latest projects -->
<h2 class="section-title" style="left:101px;top:2380px">Latest Projects</h2>
<div class="abs filters"><em>All Projects</em> / Buildings / Interior / Exterior</div>
<div class="ph" role="img" aria-label="White resort building with palms and pool" style="left:128px;top:2532px;width:179px;height:277px;background:linear-gradient(170deg,#7fa8d8,#e9e4da 55%,#2f6f93)"></div>
<div class="ph" role="img" aria-label="Modern villa with lit pool at dusk" style="left:321px;top:2532px;width:179px;height:277px;background:linear-gradient(170deg,#9eb3c9,#4b4b4b 55%,#2a9fc2)"></div>
<div class="ph" role="img" aria-label="Terraced house with pool deck" style="left:516px;top:2532px;width:179px;height:277px;background:linear-gradient(170deg,#a8cde6,#d9d4c9 55%,#3fa9c6)"></div>
<div class="ph" role="img" aria-label="Wooden cabin in snowy forest" style="left:709px;top:2532px;width:179px;height:277px;background:linear-gradient(170deg,#7aa3c9,#8a5a36 55%,#eef2f6)"></div>
<div class="ph" role="img" aria-label="Wooden cabin in snowy forest" style="left:902px;top:2532px;width:179px;height:277px;background:linear-gradient(170deg,#7aa3c9,#8a5a36 55%,#eef2f6)"></div>
<div class="abs slide-nav" style="left:128px">‹</div>
<div class="abs slide-nav" style="left:156px">›</div>

<!-- contact -->
<div class="ph contact-band" role="img" aria-label="Modern building facade at dusk" style="background:linear-gradient(100deg,#2a303a 0%,#3b4350 45%,#2a2f3a 100%)"></div>
<h2 class="section-title" style="left:78px;top:3100px;color:var(--white);font-size:42px">Contact Us</h2>
<div class="ph" role="img" aria-label="White spiral staircase interior" style="left:90px;top:3216px;width:197px;height:256px;background:linear-gradient(160deg,#f2f2f2,#a9a9a9)"></div>
<div class="contact-item">
  <svg class="abs" style="left:330px;top:3232px" width="58" height="58" viewBox="0 0 58 58"><circle cx="29" cy="29" r="27" fill="none" stroke="var(--red)" stroke-width="3"/><path d="M20 23a18 18 0 0015 15l3-3c.4-.4 1-.5 1.5-.3 1.4.5 2.4.7 3.5.7v5c-14 0-24-10-24-24h5c0 1.1.2 2.1.7 3.5.2.5.1 1.1-.3 1.5z" fill="var(--red)"/></svg>
  <h4 style="left:397px;top:3245px">Call Us</h4><p style="left:405px;top:3276px">099 555 01 40</p>
  <svg class="abs" style="left:330px;top:3326px" width="58" height="58" viewBox="0 0 58 58"><circle cx="29" cy="29" r="27" fill="none" stroke="var(--red)" stroke-width="3"/><rect x="17" y="21" width="24" height="17" fill="var(--red)"/><path d="M17 21l12 10 12-10" stroke="#fff" stroke-width="2" fill="none"/></svg>
  <h4 style="left:408px;top:3322px">Send an Email</h4><p style="left:408px;top:3353px">architektur@atelier-brunnmatt-example.ch</p>
  <svg class="abs" style="left:330px;top:3426px" width="58" height="58" viewBox="0 0 58 58"><circle cx="29" cy="29" r="27" fill="none" stroke="var(--red)" stroke-width="3"/><path d="M29 13c-6.6 0-11 4.8-11 10.8C18 32 29 45 29 45s11-13 11-21.2C40 17.8 35.6 13 29 13z" fill="var(--red)"/><circle cx="29" cy="24" r="4" fill="#fff"/></svg>
  <h4 style="left:408px;top:3422px">ServicesLocation</h4><p style="left:408px;top:3455px;font-size:12px;line-height:13px">Studio Office, Via Pradella 5<br>7499 Valmora</p>
</div>
<div class="abs form">
  <div class="field" style="top:36px">Name</div>
  <div class="field" style="top:107px">Email</div>
  <div class="field" style="top:181px">Phone</div>
  <div class="field" style="top:254px">Address</div>
  <div class="field" style="top:329px;height:103px">How we can help?</div>
  <div class="btn" style="left:130px;top:462px;width:115px;height:29px">Get a Quote</div>
</div>

<!-- blog -->
<h2 class="section-title" style="left:0;width:1200px;text-align:center;top:3783px">Latest From Blog</h2>
<div class="ph" role="img" aria-label="Living room with sofa and vase" style="left:157px;top:3927px;width:456px;height:210px;background:linear-gradient(170deg,#6f6a62,#c8c1b5 60%,#3d3934)"></div>
<div class="ph" role="img" aria-label="Dark living room with shelves" style="left:157px;top:4166px;width:456px;height:206px;background:linear-gradient(170deg,#4a4a4a,#8c8680 55%,#2c2b2a)"></div>
<div class="blog-label" style="top:4025px"><b>TITLE OF FIRST BLOG POST</b><span class="vdate" style="left:7px;top:86px">10 AUG 2023</span></div>
<div class="blog-label" style="top:4258px"><b>TITLE OF FIRST BLOG POST</b><span class="vdate" style="left:7px;top:86px">10 AUG 2023</span></div>
<div class="ph" role="img" aria-label="Small house on a hill at dusk" style="left:636px;top:3927px;width:423px;height:445px;background:linear-gradient(170deg,#4d5560,#2b3129 60%,#1c1f1a)"></div>
<div class="abs" style="left:772px;top:3986px;width:336px;height:333px;border:8px solid #000"></div>
<div class="abs" style="left:772px;top:3986px;width:300px;height:333px;background:#000;color:#fff">
  <div class="abs" style="left:32px;top:38px;font-size:25px;line-height:30px;font-weight:600;width:250px">SMALL &amp; MINIMAL HOUSE ON PATERS ON HILL</div>
  <p class="abs" style="left:32px;top:146px;width:240px;font-size:10px;line-height:20px;color:#ccc">typefaces and layouts, and in appearance of different general the content of dummy text is nonsensical typefaces of dummy text is nonsensical.</p>
  <div class="abs" style="left:32px;top:250px;font-size:10px;letter-spacing:3px;color:#ccc">READ MORE</div>
</div>
<span class="vdate" style="left:740px;top:4098px;color:#fff">10 AUG 2023</span>

<!-- footer -->
<footer class="abs footer">
  <div class="abs brand" style="left:78px;top:80px;color:#fff">ArchitekturAtelier Brunnmatt GmbH</div>
  <span class="abs" style="left:92px;top:194px;width:26px;height:26px;border-radius:50%;background:var(--red)"></span>
  <span class="abs" style="left:136px;top:194px;width:26px;height:26px;border-radius:50%;background:var(--red)"></span>
  <span class="abs" style="left:180px;top:194px;width:26px;height:26px;border-radius:50%;background:var(--red)"></span>
  <h5 style="left:367px">QUICK LINKS</h5>
  <span class="lnk" style="top:126px">HOME</span><span class="lnk" style="top:162px">SERVICES</span><span class="lnk" style="top:197px">PORTFOLIO</span><span class="lnk" style="top:233px">ABOUT</span><span class="lnk" style="top:269px">CONTACT</span>
  <h5 style="left:569px">CONTACT INFO</h5>
  <svg class="abs" style="left:570px;top:132px" width="18" height="18" viewBox="0 0 24 24"><path d="M6.6 10.8a15 15 0 006.6 6.6l2.2-2.2c.3-.3.7-.4 1-.2 1.1.4 2.3.6 3.6.6.6 0 1 .4 1 1V20c0 .6-.4 1-1 1C10.6 21 3 13.4 3 4c0-.6.4-1 1-1h3.5c.6 0 1 .4 1 1 0 1.3.2 2.5.6 3.6.1.3 0 .7-.2 1z" fill="var(--red)"/></svg>
  <span class="ci" style="top:132px">(123) 456 789</span>
  <svg class="abs" style="left:570px;top:180px" width="18" height="15" viewBox="0 0 18 15"><rect x="0" y="2" width="18" height="13" fill="var(--red)"/><path d="M0 2l9 7 9-7" stroke="#000" stroke-width="1.5" fill="none"/></svg>
  <span class="ci" style="top:178px">mail@website.com</span>
  <svg class="abs" style="left:571px;top:222px" width="16" height="22" viewBox="0 0 16 22"><path d="M8 0C3.6 0 0 3.3 0 7.6 0 13 8 22 8 22s8-9 8-14.4C16 3.3 12.4 0 8 0z" fill="var(--red)"/><circle cx="8" cy="8" r="3" fill="#000"/></svg>
  <span class="ci" style="top:220px">Harbourview Plaza, Level 2, 18 Marlow Road, Eastbrook, Queensland 4100</span>
  <h5 style="left:912px">STAY UP-TO-DATE</h5>
  <div class="abs" style="left:908px;top:146px;width:191px;height:32px;border-radius:16px;background:#444;color:#bbb;font-size:11px;display:flex;align-items:center;justify-content:center;letter-spacing:1px">EMAIL ADDRESS</div>
  <div class="abs" style="left:908px;top:192px;width:188px;height:34px;border-radius:17px;background:var(--red);color:#fff;font-size:12px;font-weight:600;display:flex;align-items:center;justify-content:center">SUBSCRIBE NOW</div>
  <div class="abs" style="left:0;top:340px;width:1200px;text-align:center;font-size:10px;color:#ccc">© 2025 ALL RIGHTS RESERVED.</div>
</footer>

</body>
</html>
```